Poster for List of Company Values

We need a poster to outline our Values which will be displayed in our office as well as posted on our website and other platforms (so need to allow for some flexibly in its application).

File attached outlines what we currently have with design and also our company style guide.

Note that we are looking for a modern, clean look, which still represents our core activities of construction and environmental services.

You can also reference our website here:

https://quorvelgroup.com.au/

Happy to answer any questions you might have.

Thanks for your interest,
Brent

Target Market(s)

Internal and External clients

Industry/Entity Type

Construction, water and recycling

Font styles to use
Sans Serif

Requirements
Must have
• All values on the one page. Graphic to represent each value. Also needs to use company logo
Nice to have
• Preference for poster to be orientated in landscape
Should not have
• Do not follow example provided, this is only to demonstrate what we have to date and also the text required

```html
<!DOCTYPE html>
<html lang="en">
<head>
<meta charset="utf-8">
<title>Quorvel Group – Our Values</title>
<link rel="stylesheet" href="https://fonts.googleapis.com/css2?family=Ubuntu:wght@500;700&display=swap">
<style>
  :root{
    --loyal:#45e800;      --loyal-deep:#3a9a1a;
    --initiative:#0019d6; --initiative-deep:#2a48f0;
    --team:#e8602e;       --team-deep:#c2481c;
    --respect:#c20e40;    --respect-deep:#7c0b36;
    --honest:#cdb830;     --honest-deep:#a8942a;
    --positive:#4a4df5;   --positive-deep:#3437dd;
    --paper:#ffffff;
    --ink:#151515;
    --brand-ink:#3a3b48;
    --brand-mark:#1d2fe0;
  }
  *{margin:0;padding:0;box-sizing:border-box}
  html,body{width:1200px;height:848px;overflow:hidden;background:var(--paper)}
  body{font-family:"Ubuntu",sans-serif;color:var(--paper)}
  .poster{position:relative;width:1200px;height:848px;background:var(--paper)}

  .value{position:absolute;width:400px;height:365px;overflow:hidden;
    clip-path:polygon(0 0,100% 0,100% calc(100% - 36px),calc(100% - 36px) 100%,0 100%)}
  .value--loyal{left:0;top:0;height:361px;background:var(--loyal)}
  .value--initiative{left:398px;top:0;height:361px;background:var(--initiative)}
  .value--team{left:800px;top:0;height:361px;background:var(--team)}
  .value--respect{left:0;top:361px;background:var(--respect)}
  .value--honest{left:398px;top:361px;background:var(--honest)}
  .value--positive{left:800px;top:361px;background:var(--positive)}

  .scene{position:absolute;bottom:0;border-radius:40% 40% 0 0 / 30% 30% 0 0}
  .value--loyal .scene{left:0;width:324px;height:168px;background:linear-gradient(180deg,rgba(58,154,26,0) 0%,var(--loyal-deep) 55%)}
  .value--initiative .scene{left:109px;width:282px;height:115px;background:linear-gradient(180deg,rgba(42,72,240,0) 0%,var(--initiative-deep) 60%)}
  .value--team .scene{left:120px;width:162px;height:152px;background:linear-gradient(180deg,rgba(194,72,28,0) 0%,var(--team-deep) 60%)}
  .value--respect .scene{left:133px;width:264px;height:203px;background:linear-gradient(180deg,rgba(124,11,54,0) 0%,var(--respect-deep) 45%)}
  .value--honest .scene{left:93px;width:298px;height:130px;background:linear-gradient(180deg,rgba(168,148,42,0) 0%,var(--honest-deep) 55%)}
  .value--positive .scene{left:146px;width:236px;height:230px;background:linear-gradient(180deg,rgba(52,55,221,0) 0%,var(--positive-deep) 50%)}

  .badge{position:absolute;width:54px;height:54px;border-radius:50%;background:var(--paper);
    box-shadow:3px 4px 5px rgba(0,0,0,.35);display:flex;align-items:center;justify-content:center}
  .badge svg{width:32px;height:32px}

  .title{position:absolute;font-weight:700;line-height:1;white-space:nowrap;
    text-shadow:2px 3px 3px rgba(0,0,0,.45);letter-spacing:-.3px}
  .title--across{font-size:38px}
  .title--stacked{font-size:41px;line-height:42px}
  .title--upright{writing-mode:vertical-rl;transform:rotate(180deg);font-size:37px;line-height:40px}

  .statement{position:absolute;font-weight:500;font-size:15px;line-height:21.5px}
</style>
</head>
<body>
<main class="poster">

  <section class="value value--loyal">
    <div class="scene" role="img" aria-label="Silhouette of tower cranes and workers on a building site"></div>
    <div class="badge" style="left:35px;top:53px">
      <svg viewBox="0 0 32 32" fill="none" stroke="var(--loyal)" stroke-width="2.4" stroke-linecap="round" stroke-linejoin="round"><path d="M3 12l6-3 5 3 5-3 7 3"/><path d="M9 12l6 6c1 1 2.5 1 3.5 0l5-5"/><path d="M3 12v8l4 2M29 12v8l-4 2"/><path d="M12 19l3 3M15 17l3 3"/></svg>
    </div>
    <h2 class="title title--across" style="left:108px;top:55px">be LOYAL</h2>
    <p class="statement" style="left:111px;top:103px">We take care of our own and<br>provide opportunities to listen<br>and support each other.</p>
  </section>

  <section class="value value--initiative">
    <div class="scene" role="img" aria-label="Silhouette of a crane, bulldozer, excavator and dump truck"></div>
    <h2 class="title title--upright" style="left:34px;top:60px;height:193px">show<br>INITIATIVE</h2>
    <div class="badge" style="left:37px;top:271px">
      <svg viewBox="0 0 32 32" fill="none" stroke="var(--initiative)" stroke-width="2.2" stroke-linecap="round"><path d="M16 9a6 6 0 0 0-3.5 10.9V22h7v-2.1A6 6 0 0 0 16 9z" fill="var(--initiative)"/><path d="M13 25h6M14 28h4M16 2v3M5 7l2 2M27 7l-2 2M2 16h3M27 16h3"/></svg>
    </div>
    <p class="statement" style="left:130px;top:102px">We celebrate and recognise<br>our own, and encourage<br>forward thinking.</p>
  </section>

  <section class="value value--team">
    <div class="scene" role="img" aria-label="Silhouette of three street traffic lights"></div>
    <div class="badge" style="left:38px;top:54px">
      <svg viewBox="0 0 32 32" fill="var(--team)"><circle cx="16" cy="7" r="3.2"/><circle cx="9" cy="9" r="2.6"/><circle cx="23" cy="9" r="2.6"/><circle cx="4" cy="11" r="2.2"/><circle cx="28" cy="11" r="2.2"/><rect x="13" y="11" width="6" height="16" rx="2.5"/><rect x="6.5" y="13" width="5" height="13" rx="2"/><rect x="20.5" y="13" width="5" height="13" rx="2"/><rect x="2" y="14.5" width="4.2" height="10" rx="1.8"/><rect x="25.8" y="14.5" width="4.2" height="10" rx="1.8"/></svg>
    </div>
    <h2 class="title title--across" style="left:106px;top:55px">think TEAM</h2>
    <p class="statement" style="left:106px;top:103px">We communicate effectively and<br>work as a team by helping and<br>supporting each other.</p>
  </section>

  <section class="value value--respect">
    <div class="scene" role="img" aria-label="Silhouette of a heavy truck with a flatbed trailer"></div>
    <h2 class="title title--upright" style="left:31px;top:42px;height:161px">show<br>RESPECT</h2>
    <div class="badge" style="left:35px;top:220px">
      <svg viewBox="0 0 32 32" fill="var(--respect)"><circle cx="11" cy="7" r="3.6"/><circle cx="21" cy="7" r="3.6"/><path d="M5 14a3 3 0 0 1 3-3h6a3 3 0 0 1 3 3v6h-2v9h-3.5v-7h-1v7H7v-9H5z"/><path d="M15 14a3 3 0 0 1 3-3h6a3 3 0 0 1 3 3v6h-2v9h-3.5v-7h-1v7H17v-9h-2z"/></svg>
    </div>
    <p class="statement" style="left:127px;top:40px">We value the diversity<br>and opinions of all.</p>
  </section>

  <section class="value value--honest">
    <div class="scene" role="img" aria-label="Silhouette of an excavator and workers on an earthworks site"></div>
    <div class="badge" style="left:37px;top:37px">
      <svg viewBox="0 0 32 32" fill="var(--honest)"><path d="M4 6h16a3 3 0 0 1 3 3v7a3 3 0 0 1-3 3h-9l-5 4v-4H4a3 3 0 0 1-3-3V9a3 3 0 0 1 3-3z"/><path d="M25 12h3a3 3 0 0 1 3 3v6a3 3 0 0 1-3 3h-1v4l-5-4h-7a3 3 0 0 1-3-3h8a5 5 0 0 0 5-5z" opacity=".75"/><circle cx="7" cy="12.5" r="1.5" fill="#fff"/><circle cx="12" cy="12.5" r="1.5" fill="#fff"/><circle cx="17" cy="12.5" r="1.5" fill="#fff"/></svg>
    </div>
    <h2 class="title title--stacked" style="left:110px;top:36px">be OPEN<br>and HONEST</h2>
    <p class="statement" style="left:113px;top:129px">We are clear and open with each<br>other, and provide an approachable<br>and friendly environment.</p>
  </section>

  <section class="value value--positive">
    <div class="scene" role="img" aria-label="Silhouette of wild grasses with a recycling arrows symbol"></div>
    <h2 class="title title--upright" style="left:36px;top:44px;height:170px">be<br>POSITIVE</h2>
    <div class="badge" style="left:38px;top:229px">
      <svg viewBox="0 0 32 32" fill="none" stroke="var(--positive)" stroke-width="2" stroke-linecap="round"><circle cx="16" cy="16" r="6" fill="var(--positive)"/><path d="M16 2v4M16 26v4M2 16h4M26 16h4M6 6l3 3M23 23l3 3M26 6l-3 3M9 23l-3 3"/><path d="M13.5 17.5q2.5 2 5 0" stroke="#fff" stroke-width="1.4"/></svg>
    </div>
    <p class="statement" style="left:126px;top:40px">We are solutions focused and<br>encourage a positive attitude<br>turning a negative into a<br>positive.</p>
  </section>

  <footer>
    <p style="position:absolute;left:42px;top:771px;font-size:20.5px;font-weight:500;color:var(--ink);white-space:nowrap">We Embody the Values of Loyalty, Initiative, Teamwork, Respect, Honesty, &amp; Positivity</p>
    <div class="brand" style="position:absolute;left:1000px;top:766px;display:flex;align-items:center;gap:12px">
      <span style="display:block;width:40px;height:40px;background:var(--brand-mark)"></span>
      <span style="font-weight:700;font-size:20px;line-height:21px;color:var(--brand-ink)">QUORVEL<br>Group</span>
    </div>
  </footer>

</main>
</body>
</html>
```